Steady Path Physical Therapy and Wellness brochure

We need a trifold brochure that would go out to physicians. I am marketing to them to get patient referrals. My business name is Steady Path Physical Therapy and Wellness, PC. We specialize in treating balance and dizziness and other neurological disorders as well as in providing general physical therapy services. We could use a logo of some sort on the brochure. Please go to steadypathpt.example and look at the about page. My business does seminars too, but I want this brochure geared to the physical therapy services we provide. The business card I attached has important information and the phone and fax number. My address is:
48207 Harlow Ridge Road, Suite #214
Laguna Niguel, CA 92640
I would like information on my business, but please include my name also. I am the sole physical therapist of the practice, but want to give the impression I am not just a small operation. I need the brochure to have Steady Path Physical Therapy and Wellness as the title, but information on me as the owner. I attached the brochure for some ideas. This is the one for my seminars. I don't want the new one geared toward seminars or this busy. However, the brochure does have some idea, like the graphic of the inner ear and then some information on me.
Thanks,
Updates
Project Deadline Extended Reason: Oh my gosh, I thought my deadline was May 13 and wanted to extend it beyond that. Can you please clarify what my deadlne is?I am new to this. Most of the designers have done something a bit different that I originally wanted.Perhaps due to language differences, this happened. However, I am liking what they have done.Please extend my deadline. I am a sole business owner.Thanks, Marla Added Wednesday, May 4, 2016
Target Market(s)
Physicians and perhaps patients
Industry/Entity Type
Business
Requirements
Must have
- My business name, my name, phone and fax, address, my picture, an about section. Not overly busy. I work with people with balance problems.
- Please state I accept Medicare Insurance. Below is on the about section.
- Doctor of Physical Therapy
- Board Certified Geriatric Specialist
- KRQP Certified for Parkinson's treatment
- Vestibular Specialist
Nice to have
- all the above. please look at my website "about section"
- It's maybe okay to mention I am a part-time University professor, but maybe not too much on this.
Should not have
- not to busy, I attached an example of a trifold brochure since it has information on me, but I don't want something this busy.

```html
<!DOCTYPE html>
<html lang="en">
<head>
<meta charset="utf-8">
<title>Steady Path Physical Therapy and Wellness – Brochure</title>
<link rel="stylesheet" href="https://fonts.googleapis.com/css2?family=Roboto+Condensed:wght@400;500&display=swap">
<style>
  :root {
    --page-bg: #1d5e8e;
    --photo-light: #eeeeec;
    --photo-mid: #dcd6cf;
    --photo-warm: #d9b99a;
    --leaf-green: #8bc34a;
    --teal: #00a78b;
    --brand-blue: #1e73b8;
    --ink: #111111;
    --paper-white: #ffffff;
  }
  * { box-sizing: border-box; margin: 0; padding: 0; }
  html, body {
    width: 1200px; height: 1200px; overflow: hidden;
    background: var(--page-bg);
    font-family: "Roboto Condensed", "Arial Narrow", sans-serif;
  }
  .brochure-frame {
    position: absolute; left: 20px; top: 150px;
    width: 1160px; height: 900px;
    box-shadow: 0 24px 40px rgba(0,0,0,0.35);
  }
  .brochure {
    position: absolute; left: 0; top: 0;
    width: 1340px; height: 1040px;
    transform: scale(0.86567); transform-origin: 0 0;
    overflow: hidden;
  }
  .brochure-art { position: absolute; inset: 0; }
  .brand {
    position: absolute; left: 80px; top: 52px;
    display: flex; align-items: center; gap: 40px;
  }
  .brand-dot {
    width: 138px; height: 138px; border-radius: 50%;
    background: var(--leaf-green); flex: none;
  }
  .brand-name {
    color: var(--brand-blue);
    font-size: 30px; font-weight: 400; line-height: 38px;
    text-transform: uppercase; width: 640px;
  }
  .about {
    position: absolute; left: 56px; top: 570px; width: 790px;
    color: var(--paper-white);
  }
  .section-title {
    color: var(--ink); font-weight: 400; font-size: 52px; line-height: 60px;
    margin-left: 4px; margin-bottom: 6px;
  }
  .body-copy {
    font-size: 15.6px; line-height: 20px; text-align: justify;
  }
  .owner-lead {
    color: var(--ink); font-size: 21.5px; line-height: 26px;
    margin: 18px 0 0 3px; width: 740px;
  }
  .owner-detail {
    font-size: 15.6px; line-height: 20px; margin: 25px 0 0 3px; text-align: justify;
  }
  .contact {
    position: absolute; left: 934px; top: 566px; width: 390px;
    color: var(--paper-white);
  }
  .contact .section-title { margin-left: 0; margin-bottom: 10px; font-size: 50px; }
  .contact-lines { font-size: 16px; line-height: 20px; }
  .credentials-title {
    color: var(--ink); font-weight: 400; font-size: 34px; line-height: 40px;
    margin: 26px 0 10px -3px;
  }
  .credential-line { font-size: 21px; line-height: 26px; }
  .insurance-note { font-size: 16px; line-height: 20px; margin-top: 8px; }
  .web-address { font-size: 21px; line-height: 30px; margin-top: 2px; }
</style>
</head>
<body>
  <div class="brochure-frame">
    <div class="brochure">
      <svg class="brochure-art" viewBox="0 0 1340 1040" width="1340" height="1040">
        <defs>
          <linearGradient id="photoTone" x1="0" y1="0" x2="1" y2="0.3">
            <stop offset="0" stop-color="#eeeeec"/>
            <stop offset="0.5" stop-color="#dcd6cf"/>
            <stop offset="0.85" stop-color="#d9b99a"/>
            <stop offset="1" stop-color="#9a9a98"/>
          </linearGradient>
        </defs>
        <rect class="treatment-photo" x="0" y="0" width="1340" height="600" fill="url(#photoTone)"
              role="img" aria-label="Photograph of a therapist treating a patient's lower back on a treatment table in a bright clinic room"/>
        <path class="green-wave" fill="#8bc34a"
              d="M0,402 C150,520 330,590 500,580 C650,572 780,555 881,548 L1340,548 L1340,1040 L0,1040 Z"/>
        <path class="teal-panel" fill="#00a78b"
              d="M888,545 C1050,524 1200,506 1340,502 L1340,1019 L888,1019 Z"/>
        <rect class="fold-panel" x="443" y="0" width="438" height="1040" fill="#ffffff" opacity="0.07"/>
        <line class="fold-line" x1="443" y1="0" x2="443" y2="1040" stroke="#000" stroke-opacity="0.06" stroke-width="2"/>
        <line class="fold-line" x1="881" y1="0" x2="881" y2="1040" stroke="#000" stroke-opacity="0.06" stroke-width="2"/>
      </svg>

      <div class="brand">
        <span class="brand-dot"></span>
        <h1 class="brand-name">Steady Path Physical Therapy and Wellness, Professional Corporation</h1>
      </div>

      <section class="about">
        <h2 class="section-title">About Our Practice</h2>
        <p class="body-copy">Vestibular and balance disorders can cause disturbing symptoms such as dizziness, vertigo, nausea, anxiety, fatigue and imbalance. The related impairments can lead to functional limitations, disability and falls that can be devastating. These problems are frequently not diagnosed or treated properly and in a timely manner. At Steady Path Physical Therapy and Wellness we specialize in the evaluation and treatment of balance and dizziness disorders and other neurological conditions, including stroke, head injury and Parkinson's disease, as well as providing general physical therapy services. Each patient receives a detailed examination and a specific exercise program addressing their individual impairments, with the goal of decreasing dizziness, improving balance, reducing the risk of falls and improving quality of life. We welcome physician referrals and work closely with each referring provider.</p>
        <p class="owner-lead">Owner and treating therapist: Marla Quenby, PT, DPT – providing one-on-one care for every patient.</p>
        <p class="owner-detail">Dr. Quenby is a Doctor of Physical Therapy and a Board Certified Geriatric Specialist with advanced training in vestibular rehabilitation and KRQP certification for Parkinson's treatment. She also teaches part time as a university professor, bringing current research directly into her patient care.</p>
      </section>

      <section class="contact">
        <h2 class="section-title">Contact</h2>
        <p class="contact-lines">
          Phone: (949) 555-0178<br>
          Fax: (949) 555-0179<br>
          Steady Path PT and Wellness<br>
          48207 Harlow Ridge Road, Suite #214<br>
          Laguna Niguel, CA 92640-1185
        </p>
        <h3 class="credentials-title">Credentials:</h3>
        <p class="credential-line">Doctor of Physical Therapy</p>
        <p class="credential-line">Board Certified Geriatric Specialist</p>
        <p class="credential-line">KRQP Certified for Parkinson's</p>
        <p class="credential-line">Vestibular Specialist</p>
        <p class="insurance-note">We accept Medicare Insurance.</p>
        <p class="web-address">www.steadypathpt.example</p>
      </section>
    </div>
  </div>
</body>
</html>
```